Website for a Construction Business That Builds Houses

We want some design concepts for this website. Customer likes this competitor site: https://copperfernbuilds.com.au/

We have a logo for Varrow Constructions. Logo font is Birdman, attached with AI.

Want to be able to change hero images

Will have a contact page.

Need to know what plugins will be used for WordPress.

```html
<!DOCTYPE html>
<html lang="en">
<head>
<meta charset="utf-8">
<title>Varrow Constructions</title>
<link href="https://fonts.googleapis.com/css2?family=Playfair+Display:wght@500;600;700&family=Montserrat:wght@400;500;600&display=swap" rel="stylesheet">
<style>
:root{
  --green:#8cc63f;
  --dark:#1b1b1b;
  --ink:#222222;
  --muted:#7a7a7a;
  --soft:#f4f4f4;
  --field:#f1f1f1;
  --white:#ffffff;
}
*{box-sizing:border-box;margin:0;padding:0}
html,body{width:1200px;height:5088px;overflow:hidden}
body{position:relative;background:var(--white);font-family:"Montserrat",sans-serif;color:var(--ink)}
.abs{position:absolute}
.btn{position:absolute;display:flex;align-items:center;justify-content:center;font-size:15px;font-weight:500;letter-spacing:.5px;text-transform:uppercase;color:var(--white);background:var(--green);white-space:nowrap}
.btn.outline{background:transparent;border:3px solid var(--white)}
.btn.outline-green{background:transparent;border:3px solid var(--green);color:var(--green)}
.photo{position:absolute}

/* top bar */
.topbar{left:0;top:0;width:1200px;height:50px;background:var(--green);color:var(--white);font-size:16px;font-weight:500}
.topbar .item{position:absolute;top:14px;display:flex;align-items:center;gap:10px}
.social{position:absolute;display:flex;gap:26px}
.social span{width:14px;height:14px;border-radius:50%;border:2px solid currentColor;display:block}

/* nav */
.nav a{position:absolute;top:94px;font-family:"Playfair Display",serif;font-size:16px;font-weight:600;color:var(--ink);text-decoration:none;white-space:nowrap}
.brand-mark{position:absolute;border-radius:50%;background:var(--white);display:flex;align-items:center;justify-content:center;text-align:center;font-family:"Montserrat",sans-serif;font-weight:600;color:#444;line-height:1.15}

/* hero */
.hero-frame{left:40px;top:195px;width:1108px;height:585px;border:2px solid var(--white)}
.hero-card{left:100px;top:345px;width:505px;height:295px;background:var(--green);color:var(--white);padding:46px 40px 0 42px}
.hero-card h1{font-family:"Playfair Display",serif;font-weight:600;font-size:41px;line-height:1.1;white-space:nowrap;margin-bottom:16px}
.hero-card p{font-size:15px;line-height:26px}
.hero-card .btn{position:relative;margin-top:20px;width:155px;height:40px}
.dots{left:556px;top:797px;display:flex;gap:8px}
.dots span{width:14px;height:14px;background:var(--white);display:block}
.dots span.on{background:var(--green)}

.eyebrow{position:absolute;font-size:16px;color:var(--green);letter-spacing:.3px;white-space:nowrap}
.title{position:absolute;font-family:"Playfair Display",serif;font-weight:600;font-size:33px;line-height:41px;color:var(--ink);white-space:nowrap}
.para{position:absolute;font-size:15px;line-height:26px;color:var(--muted)}

.card{position:absolute;top:2250px;width:302px;height:495px;background:var(--white);box-shadow:0 4px 18px rgba(0,0,0,.08)}
.card .photo{left:0;top:0;width:302px;height:250px}
.card h3{position:absolute;top:278px;left:0;width:100%;text-align:center;font-family:"Playfair Display",serif;font-weight:600;font-size:24px;line-height:31px}
.card p{position:absolute;top:345px;left:22px;width:258px;text-align:center;font-size:10px;line-height:14px;color:var(--muted)}
.card .btn{left:62px;top:435px;width:176px;height:40px}

.field{position:absolute;background:var(--field);font-size:10px;color:#777;padding:6px 12px}

.footer{left:0;top:4708px;width:1200px;height:380px;background:var(--dark);color:var(--white)}
.footer h4{position:absolute;font-family:"Playfair Display",serif;font-weight:600;font-size:20px;white-space:nowrap}
.footer .line{position:absolute;font-size:13px;display:flex;align-items:center;gap:14px;white-space:nowrap}
</style>
</head>
<body>

<div class="abs topbar">
  <div class="item" style="left:28px">
    <svg width="22" height="22" viewBox="0 0 24 24" fill="#fff"><path d="M6.6 10.8a15 15 0 0 0 6.6 6.6l2.2-2.2c.3-.3.7-.4 1-.2 1.1.4 2.3.6 3.6.6.6 0 1 .4 1 1V20c0 .6-.4 1-1 1A17 17 0 0 1 3 4c0-.6.4-1 1-1h3.5c.6 0 1 .4 1 1 0 1.3.2 2.5.6 3.6.1.3 0 .7-.2 1z"/></svg>
    <span>+61 3 9014 2275</span>
  </div>
  <div class="item" style="left:280px">
    <svg width="24" height="18" viewBox="0 0 24 18"><rect x="1" y="1" width="22" height="16" fill="#fff"/><path d="M1 1l11 9 11-9" fill="none" stroke="#8cc63f" stroke-width="2"/></svg>
    <span>support@domain.com</span>
  </div>
  <div class="social" style="left:1052px;top:18px;color:#fff"><span></span><span></span><span></span></div>
</div>

<nav class="nav">
  <a style="left:30px">Home</a>
  <a style="left:118px">About</a>
  <a style="left:205px">Home Designs</a>
  <a style="left:352px">Display Homes</a>
  <a style="left:718px">Custom Build</a>
  <a style="left:860px">House Rebuild</a>
</nav>
<div class="btn" style="left:1015px;top:88px;width:153px;height:38px">Contact Us</div>

<div class="photo" role="img" aria-label="Living room with timber-panelled walls, grey sofa and track lighting" style="left:0;top:155px;width:1200px;height:675px;background:linear-gradient(100deg,#3b3026 0%,#6e5a45 35%,#9a8570 60%,#cfc6ba 80%,#8a7764 100%)"></div>
<div class="abs hero-frame"></div>
<div class="abs hero-card">
  <h1>Varrow Constructions</h1>
  <p>Building your own home is an experience of a lifetime. Who you choose to work with on your journey can make the world of difference.</p>
  <div class="btn outline">Contact Us</div>
</div>
<div class="abs dots"><span></span><span></span><span class="on"></span><span></span><span></span></div>

<div class="brand-mark" style="left:508px;top:58px;width:184px;height:184px;font-size:18px;box-shadow:0 0 0 1px #eee">Varrow<br>Constructions</div>

<div class="abs" style="left:98px;top:948px;width:348px;height:470px;border:14px solid var(--green)"></div>
<div class="photo" role="img" aria-label="Modern living room with fireplace, timber ceiling and white armchair" style="left:146px;top:1036px;width:404px;height:404px;background:linear-gradient(160deg,#5b4b3c 0%,#8f7f6c 45%,#c9bfb2 75%,#6b6258 100%)"></div>
<h2 class="title" style="left:602px;top:1080px">Embrace the joy of your new home.</h2>
<p class="para" style="left:603px;top:1140px;width:560px">Building your own home is an experience of a lifetime. Who you choose to work with on your journey can make the world of difference. At Copperfern Homes our focus is you, the client. We work hard to ensure you're delighted—not just with the end result—but with the entire building process.</p>
<div class="btn" style="left:608px;top:1272px;width:175px;height:40px">Read More</div>

<div class="abs" style="left:0;top:1585px;width:612px;height:455px;background:var(--soft)"></div>
<div class="photo" role="img" aria-label="Lavender living room with blue sofa, wall shelves and framed prints" style="left:612px;top:1585px;width:588px;height:455px;background:linear-gradient(170deg,#b9bdf0 0%,#8c93d8 45%,#6f76bf 70%,#c9c9d2 100%)"></div>
<div class="eyebrow" style="left:145px;top:1688px">Knock Down Rebuild</div>
<h2 class="title" style="left:141px;top:1726px;font-size:34px">Check out our<br>latest knockdown<br>rebuild project here.</h2>
<div class="btn" style="left:141px;top:1873px;width:176px;height:40px">Read More</div>
<div class="btn outline-green" style="left:327px;top:1873px;width:177px;height:40px">Watch Video</div>

<h2 class="title" style="left:0;top:2143px;width:1200px;text-align:center;font-size:32px">A package that fits any budget.</h2>
<div class="card" style="left:102px">
  <div class="photo" role="img" aria-label="Contemporary two-storey home with timber cladding beside a pool" style="background:linear-gradient(160deg,#cfd8e2 0%,#a8a59e 45%,#7a5a40 75%,#4a7aa0 100%)"></div>
  <h3>A new level of<br>inspired living.</h3>
  <p>The Aspect range offer great affordability coupled with stylish finishes that are perfectly suited for the growing family, first timers or savvy investors.</p>
  <div class="btn">Read More</div>
</div>
<div class="card" style="left:452px">
  <div class="photo" role="img" aria-label="Modern grey and timber facade with manicured hedges" style="background:linear-gradient(170deg,#e6e8ea 0%,#b7b5b1 45%,#5d4a3c 70%,#2e3a2a 100%)"></div>
  <h3>Live a life that<br>stands out.</h3>
  <p>The Aspect range offer great affordability coupled with stylish finishes that are perfectly suited for the growing family, first timers or savvy investors.</p>
  <div class="btn">Read More</div>
</div>
<div class="card" style="left:806px">
  <div class="photo" role="img" aria-label="Timber-walled lounge with sofa and large black-framed windows" style="background:linear-gradient(110deg,#2f2a25 0%,#7a6b5a 40%,#b8a994 70%,#d8d2c8 100%)"></div>
  <h3>An inspired level<br>of living</h3>
  <p>The Aspect range offer great affordability coupled with stylish finishes that are perfectly suited for the growing family, first timers or savvy investors.</p>
  <div class="btn">Read More</div>
</div>

<div class="photo" role="img" aria-label="Two-storey white and timber home at dusk with hedges" style="left:0;top:2888px;width:573px;height:455px;background:linear-gradient(175deg,#eef0f0 0%,#c9ccca 40%,#6e5b4b 65%,#263021 100%)"></div>
<div class="abs" style="left:573px;top:2888px;width:627px;height:455px;background:var(--green)"></div>
<div class="eyebrow" style="left:731px;top:2988px;color:#fff">CUSTOM DESIGN</div>
<h2 class="title" style="left:728px;top:3022px;color:#fff;font-size:34px">Beautifully crafted<br>luxury homes you'll<br>fall in love with.</h2>
<div class="btn outline" style="left:727px;top:3170px;width:176px;height:40px">Read More</div>

<div class="eyebrow" style="left:105px;top:3480px">DESIGN STUDIO</div>
<h2 class="title" style="left:102px;top:3515px;font-size:34px">Luxury hand crafted<br>homes that you will<br>fall in love with</h2>
<div class="btn" style="left:103px;top:3660px;width:170px;height:38px">Read More</div>
<div class="photo" role="img" aria-label="Open living room with timber ceiling, tufted ottoman and pool view" style="left:573px;top:3343px;width:627px;height:455px;background:linear-gradient(160deg,#7a4a2a 0%,#a06a40 35%,#c9b8a2 65%,#5c7a4a 100%)"></div>

<div class="photo" role="img" aria-label="Dark timber modern home at twilight with lawn and pool" style="left:0;top:3798px;width:573px;height:455px;background:linear-gradient(180deg,#a9bccb 0%,#6c7a86 40%,#3a3f44 65%,#4f6a3c 100%)"></div>
<div class="eyebrow" style="left:743px;top:3935px">LUXURY LIVING</div>
<h2 class="title" style="left:740px;top:3970px;font-size:34px">Luxury hand crafted<br>homes that you will<br>fall in love with</h2>
<div class="btn" style="left:740px;top:4120px;width:175px;height:40px">Read More</div>

<h2 class="title" style="left:0;top:4340px;width:545px;text-align:center;font-size:32px">Get in touch</h2>
<div class="field" style="left:58px;top:4410px;width:205px;height:26px">Your Name</div>
<div class="field" style="left:290px;top:4410px;width:203px;height:26px">Your Phone</div>
<div class="field" style="left:58px;top:4454px;width:205px;height:26px">Email Address</div>
<div class="field" style="left:290px;top:4454px;width:203px;height:26px">Select Service</div>
<div class="field" style="left:58px;top:4497px;width:435px;height:50px">Additional Message</div>
<div class="btn" style="left:58px;top:4575px;width:435px;height:38px">Get an Appointment Now</div>
<div class="photo" role="img" aria-label="Road map of northern Australia showing the office region" style="left:573px;top:4253px;width:627px;height:455px;background:linear-gradient(135deg,#eef0e6 0%,#e4e8da 50%,#f0ede2 100%)"></div>

<footer class="abs footer">
  <div class="brand-mark" style="left:52px;top:120px;width:156px;height:156px;font-size:15px">Varrow<br>Constructions</div>
  <h4 style="left:318px;top:98px">Contact us</h4>
  <div class="line" style="left:320px;top:163px">
    <svg width="18" height="18" viewBox="0 0 24 24" fill="#8cc63f"><path d="M6.6 10.8a15 15 0 0 0 6.6 6.6l2.2-2.2c.3-.3.7-.4 1-.2 1.1.4 2.3.6 3.6.6.6 0 1 .4 1 1V20c0 .6-.4 1-1 1A17 17 0 0 1 3 4c0-.6.4-1 1-1h3.5c.6 0 1 .4 1 1 0 1.3.2 2.5.6 3.6.1.3 0 .7-.2 1z"/></svg>(+61) 3 9014 2276</div>
  <div class="line" style="left:320px;top:210px">
    <svg width="18" height="14" viewBox="0 0 24 18"><rect x="1" y="1" width="22" height="16" fill="#8cc63f"/><path d="M1 1l11 9 11-9" fill="none" stroke="#1b1b1b" stroke-width="2"/></svg>support@domain.com</div>
  <div class="line" style="left:320px;top:256px">
    <svg width="16" height="20" viewBox="0 0 16 22"><path d="M8 0a8 8 0 0 1 8 8c0 6-8 14-8 14S0 14 0 8a8 8 0 0 1 8-8z" fill="#8cc63f"/><circle cx="8" cy="8" r="3" fill="#1b1b1b"/></svg>48 Larkspur Road, Ashvale</div>
  <h4 style="left:653px;top:100px">Quick Links</h4>
  <div class="line" style="left:653px;top:165px">Home</div>
  <div class="line" style="left:653px;top:197px">About</div>
  <div class="line" style="left:653px;top:229px">Services</div>
  <div class="line" style="left:651px;top:261px">Contact</div>
  <h4 style="left:925px;top:100px">Connect with us</h4>
  <div class="social" style="left:930px;top:170px;gap:40px;color:#8cc63f"><span style="width:18px;height:18px"></span><span style="width:18px;height:18px"></span><span style="width:18px;height:18px"></span></div>
</footer>

</body>
</html>
```